Flyer Promoting Dental Benefit Program

I want to promote a dental benefit program to my patients that do not have dental insurance. This flyer would be posted in our waiting room and where people make payments. The goal would be to get those interested to request more information and enroll in the program. I have a card that will be issued that has a logo. Theflyer and card should feel congruent. I've uploaded a file with a copy of that card.
The plan costs $290/person. It includes 2 cleanings, exams, and x-rays. It also includes a 20% discount off of our standard fees. The plan or membership lasts for one year. It is only available to those without insurance. It is also important to let people know that this is not insurance (some kind of a disclaimer).
Updates
This plan is only available to patients at my office. The contact information is: Harborview Dental, 2718 West 4600 North Suite 209, Salt Lake City, Utah 84196. (801) 555-0187. info@harborviewdentalexample.com. It is not necessary to include contact information as this flyer will be used as in-office promotion.
Target Market(s)
Those without dental insurance, but have resources to afford dental care.
Industry/Entity Type
Insurance
Look and feel
Each slider illustrates characteristics of the customer's brand and the style your logo design should communicate.

```html
<!DOCTYPE html>
<html lang="en">
<head>
<meta charset="utf-8">
<title>BrightPath Dental Plan Flyer</title>
<link rel="stylesheet" href="https://fonts.googleapis.com/css2?family=Arimo:wght@700&family=Source+Sans+3:wght@400;600;700&family=Lora:ital@1&display=swap">
<style>
  :root {
    --green: #3f9b3f;
    --green-bright: #4caf3f;
    --charcoal: #333333;
    --ink: #1e1e1e;
    --paper: #ffffff;
    --muted: #6a6a6a;
  }
  html, body {
    margin: 0;
    padding: 0;
    width: 931px;
    height: 1200px;
    overflow: hidden;
    background: var(--paper);
  }
  .flyer {
    position: relative;
    width: 931px;
    height: 1200px;
    background: var(--paper);
    overflow: hidden;
  }
  .flyer-art {
    position: absolute;
    inset: 0;
    width: 931px;
    height: 1200px;
  }
  .headline {
    position: absolute;
    left: 20px;
    top: 648px;
    width: 345px;
    margin: 0;
    text-align: center;
    font-family: "Arimo", Arial, sans-serif;
    font-weight: 700;
    font-size: 45px;
    line-height: 76.5px;
    color: var(--green);
  }
  .program-name {
    position: absolute;
    left: 590px;
    top: 662px;
    margin: 0;
    font-family: "Source Sans 3", Arial, sans-serif;
    font-weight: 700;
    font-size: 42px;
    line-height: 44px;
    color: var(--charcoal);
  }
  .discount-badge {
    position: absolute;
    left: 408px;
    top: 858px;
    width: 216px;
    height: 216px;
    display: flex;
    flex-direction: column;
    align-items: center;
    justify-content: center;
    text-align: center;
    color: var(--paper);
  }
  .discount-badge .amount,
  .discount-badge .label {
    font-family: "Source Sans 3", Arial, sans-serif;
    font-weight: 700;
    font-size: 34px;
    line-height: 34px;
  }
  .discount-badge .terms {
    margin-top: 4px;
    font-family: "Lora", Georgia, serif;
    font-style: italic;
    font-size: 23px;
    line-height: 25px;
  }
  .includes {
    position: absolute;
    left: 650px;
    top: 905px;
    font-family: "Source Sans 3", Arial, sans-serif;
    color: var(--charcoal);
  }
  .includes-title {
    margin: 0 0 4px;
    font-weight: 400;
    font-size: 28px;
    line-height: 36px;
  }
  .includes-list {
    list-style: none;
    margin: 0;
    padding: 0;
  }
  .includes-list li {
    position: relative;
    padding-left: 30px;
    font-size: 30px;
    line-height: 37px;
    font-weight: 400;
    text-transform: uppercase;
  }
  .includes-list li::before {
    content: "";
    position: absolute;
    left: 0;
    top: 11px;
    width: 16px;
    height: 16px;
    border-radius: 50%;
    background: var(--green-bright);
  }
  .disclaimer {
    position: absolute;
    left: 412px;
    top: 1098px;
    width: 500px;
    margin: 0;
    font-family: "Source Sans 3", Arial, sans-serif;
    font-size: 15.5px;
    line-height: 20px;
    color: var(--ink);
  }
</style>
</head>
<body>
<main class="flyer">
  <svg class="flyer-art" viewBox="0 0 931 1200" xmlns="http://www.w3.org/2000/svg">
    <defs>
      <linearGradient id="photo-tones" x1="0" y1="0" x2="1" y2="1">
        <stop offset="0" stop-color="#8fae63"/>
        <stop offset="0.45" stop-color="#c9a48c"/>
        <stop offset="0.75" stop-color="#d9dee0"/>
        <stop offset="1" stop-color="#7f9f55"/>
      </linearGradient>
    </defs>
    <path class="dark-band" d="M0 540 C 120 575, 260 612, 420 608 C 600 604, 780 540, 931 505 V 560 C 780 590, 600 640, 420 645 C 260 648, 120 615, 0 588 Z" fill="#3a3a3a"/>
    <path class="green-band" d="M0 500 C 120 535, 250 570, 400 572 C 600 574, 780 490, 931 430 V 520 C 780 560, 600 610, 420 612 C 260 614, 120 580, 0 548 Z" fill="#45a040"/>
    <path class="photo" role="img" aria-label="Photo of a smiling couple outdoors, a woman in a pink top leaning on a man in a white shirt" d="M0 0 H931 V430 C 780 490, 600 560, 400 560 C 250 560, 120 530, 0 500 Z" fill="url(#photo-tones)"/>
    <circle class="program-mark" cx="520" cy="706" r="66" fill="#4caf3f"/>
    <circle class="discount-ring" cx="516" cy="966" r="106" fill="#333333" stroke="#4caf3f" stroke-width="13"/>
  </svg>

  <h1 class="headline">Dental<br>benefit<br>program to<br>my patients<br>that do not<br>have dental<br>insurance</h1>

  <p class="program-name">BrightPath<br>Dental Plan</p>

  <div class="discount-badge">
    <span class="amount">20%</span>
    <span class="label">discount</span>
    <span class="terms">off our<br>standard<br>fees.</span>
  </div>

  <section class="includes">
    <p class="includes-title">it includes</p>
    <ul class="includes-list">
      <li>2 Cleanings</li>
      <li>Exams</li>
      <li>X-Rays</li>
    </ul>
  </section>

  <p class="disclaimer">The plan or membership lasts for one year. It is only available to those without insurance. It is also important to let people know that this is not insurance (some kind of a disclaimer).</p>
</main>
</body>
</html>
```